Lighting Product Brochure Design

We need a brochure templete design for a new LED public lighting product range. Products are called 'Quorivanta'.

We would like to see designs that are professional, simple, and impressive. Light color schemes are preferred. The finished design is preferably an editable template used within Word processors.

Basic product specification, logo and pictures enclosed. There will be not restriction on how the specification is presented in the brochure as long as it serves the purpose. A brochure sample has also been uploaded for reference only.

Please find short video footage to show you some of our projects in New Zealand:

https://files.vexamoor.net/item/q7Rm2KxwPz8Ld5NbTc4YhGs3VfJe9Ua6M/open?mode=public

Target Market(s)

Contractors, Councils, Private Utilities Companies.

Industry/Entity Type

Lighting Fixture

Font styles to use
Sans Serif

Requirements
Must have
• Product specificaiton, charts, drawings/pictures.

```html
<!DOCTYPE html>
<html lang="en">
<head>
<meta charset="utf-8">
<title>Quorivanta LED Streetlights – Product Specification</title>
<link href="https://fonts.googleapis.com/css2?family=Montserrat:wght@400;500;600;700;800&display=swap" rel="stylesheet">
<style>
  :root{
    --brand-blue:#0a5aa5;
    --brand-navy:#0b3a75;
    --heading-blue:#1a3d8a;
    --ink:#333840;
    --muted:#5a6068;
    --rule:#b9bcc2;
    --row-shade:#efefef;
    --canvas:#efefef;
    --paper:#ffffff;
    --chart-fill:#e6ebf3;
  }
  *{box-sizing:border-box;margin:0;padding:0}
  html,body{width:1200px;height:3000px;overflow:hidden}
  body{background:var(--canvas);font-family:"Montserrat",Arial,sans-serif;color:var(--ink);position:relative}

  .page{position:absolute;left:353px;width:494px;height:699px;background:var(--paper);overflow:hidden;box-shadow:2px 3px 5px rgba(0,0,0,.28)}
  .page--cover{top:36px;background:var(--brand-blue)}
  .page--notice{top:776px}
  .page--nomenclature{top:1517px}
  .page--back{top:2257px;background:var(--brand-blue)}
  .page-shapes{position:absolute;left:0;top:0;width:494px;height:699px}
  .abs{position:absolute}

  /* cover */
  .cover-title{left:43px;top:92px;color:#fff;line-height:1}
  .cover-title__line1{font-size:29px;font-weight:600;letter-spacing:.5px;display:block}
  .cover-title__line2{font-size:28px;font-weight:800;display:block;margin-top:8px}
  .cover-rule{left:43px;top:166px;width:134px;height:3px;background:#fff}
  .cover-intro{left:43px;top:185px;width:365px;font-size:7px;line-height:11px;color:#fff;font-weight:500}
  .product-photo{background:#fff;border:none}
  .product-photo__fill{position:absolute;inset:6px;background:linear-gradient(180deg,#f2f4f7,#d8dde4)}
  .wordmark{font-size:27px;font-weight:800;letter-spacing:.5px;line-height:1}
  .wordmark--dark{color:#1d1f24}
  .wordmark--light{color:#fff}
  .cover-url{left:43px;top:651px;font-size:10px;color:#333}
  .badges{left:262px;top:650px;display:flex;gap:8px;align-items:center}
  .badge{width:15px;height:15px;border-radius:50%;background:#8b9099}

  /* inner pages */
  .section-title{font-size:13px;color:var(--heading-blue);font-weight:400;letter-spacing:.3px}
  .section-title b{font-weight:700;position:relative;display:inline-block}
  .section-title b::after{content:"";position:absolute;left:0;right:0;bottom:-5px;height:2.5px;background:var(--heading-blue)}
  .notice-list{left:35px;top:83px;width:420px;list-style:none}
  .notice-list li{position:relative;padding-left:18px;font-size:8.4px;line-height:10.8px;color:var(--ink);margin-bottom:10px}
  .notice-list svg{position:absolute;left:0;top:1px;width:10px;height:10px}

  table{border-collapse:collapse;table-layout:fixed}
  .spec-table{left:35px;top:326px;width:425px;height:298px;border:1.5px solid var(--rule)}
  .spec-table th,.spec-table td{border:1px solid var(--rule);text-align:center;font-size:7.4px;color:var(--ink)}
  .spec-table th{font-weight:600;height:51px;line-height:10px}
  .spec-table tbody tr:nth-child(even) td.shade{background:var(--row-shade)}
  .spec-table td.merged{background:#fff}

  .nomen-table{left:33px;top:79px;width:428px;height:97px;border:1.5px solid var(--rule)}
  .nomen-table td{border:1px solid var(--rule);text-align:center;font-size:8px;color:var(--ink)}
  .nomen-table td.label{font-weight:600}
  .group-table{left:33px;top:199px;width:428px;height:200px;border:1.5px solid var(--rule)}
  .group-table th,.group-table td{border:1px solid var(--rule);font-size:7.4px;color:var(--ink)}
  .group-table th{font-weight:600;text-align:center;height:28px}
  .group-table td.code{font-weight:600;text-align:center;width:77px}
  .group-table td.desc{padding:0 18px;line-height:9px}
  .group-table tbody tr:nth-child(even) td{background:var(--row-shade)}

  .chart-caption{font-size:8.4px;color:var(--brand-blue);text-align:center;width:140px}
  .chart{background:var(--chart-fill);border:1px solid #d3d9e3}

  .page-number{left:35px;top:664px;width:30px;height:35px;background:var(--brand-navy);color:#fff;font-size:12px;display:flex;align-items:center;justify-content:center}
  .page-url{right:34px;top:675px;font-size:8.4px;color:#333;display:flex;align-items:center;gap:5px}
  .page-url::before{content:"";width:6px;height:6px;border-radius:50%;background:var(--brand-blue)}

  /* back */
  .back-mark{left:0;width:494px;top:196px;text-align:center}
  .contact-row{left:62px;top:640px;display:flex;align-items:center;gap:20px;font-size:7px;color:var(--brand-navy)}
  .contact-item{display:flex;align-items:center;gap:6px;line-height:8.5px}
  .contact-item svg{width:9px;height:9px;flex:none}
</style>
</head>
<body>

<!-- Cover -->
<section class="page page--cover">
  <svg class="page-shapes" viewBox="0 0 424 600" preserveAspectRatio="none" aria-hidden="true">
    <polygon points="194,332 424,450 424,600 194,372" fill="#0b3a75"/>
    <polygon points="0,372 194,282 194,300 0,462" fill="#0b3a75"/>
    <polygon points="0,462 194,300 424,600 0,600" fill="#ffffff"/>
  </svg>
  <h1 class="abs cover-title">
    <span class="cover-title__line1">LED STREETLIGHTS</span>
    <span class="cover-title__line2">PRODUCT SPECIFICATION</span>
  </h1>
  <div class="abs cover-rule"></div>
  <p class="abs cover-intro">Quorivanta Lighting offers distinguished and innovative outdoor lighting solutions that are ready to meet the challenges of today and tomorrow. We produce public lights and street lights across Australia and New Zealand that are energy efficient, cost-effective, and built to last.</p>
  <div class="abs product-photo" style="left:70px;top:269px;width:151px;height:56px" role="img" aria-label="Side view of an LED streetlight luminaire"><div class="product-photo__fill"></div></div>
  <div class="abs product-photo" style="left:70px;top:347px;width:156px;height:134px;border:3px solid #0b3a75" role="img" aria-label="Three LED streetlight luminaires in different sizes"><div class="product-photo__fill"></div></div>
  <div class="abs wordmark wordmark--dark" style="left:43px;top:600px">Quorivanta</div>
  <div class="abs cover-url">www.quorivanta.co.nz</div>
  <div class="abs badges" aria-label="Certifications">
    <span class="badge"></span><span class="badge"></span><span class="badge"></span><span class="badge"></span><span class="badge"></span>
  </div>
</section>

<!-- Important notice -->
<section class="page page--notice">
  <h2 class="abs section-title" style="left:35px;top:46px"><b>IMPORTANT</b> NOTICE</h2>
  <ul class="abs notice-list">
    <li><svg viewBox="0 0 10 10"><rect x="0.7" y="0.7" width="8.6" height="8.6" fill="none" stroke="#1a3d8a" stroke-width="1.2"/><path d="M2.3 5l2 2 4-5" fill="none" stroke="#1a3d8a" stroke-width="1.4"/></svg>To reduce the risk of electric shock, disconnect power supply before installation or servicing.</li>
    <li><svg viewBox="0 0 10 10"><rect x="0.7" y="0.7" width="8.6" height="8.6" fill="none" stroke="#1a3d8a" stroke-width="1.2"/><path d="M2.3 5l2 2 4-5" fill="none" stroke="#1a3d8a" stroke-width="1.4"/></svg>This luminaire must be installed in accordance with the local electrical code. If you are not familiar with these codes and requirements, consult a qualified electrician.</li>
    <li><svg viewBox="0 0 10 10"><rect x="0.7" y="0.7" width="8.6" height="8.6" fill="none" stroke="#1a3d8a" stroke-width="1.2"/><path d="M2.3 5l2 2 4-5" fill="none" stroke="#1a3d8a" stroke-width="1.4"/></svg>If NEMA photo control is installed refer to NEMA Receptacle section for instructions.</li>
    <li><svg viewBox="0 0 10 10"><rect x="0.7" y="0.7" width="8.6" height="8.6" fill="none" stroke="#1a3d8a" stroke-width="1.2"/><path d="M2.3 5l2 2 4-5" fill="none" stroke="#1a3d8a" stroke-width="1.4"/></svg>If mounting bolts are completely removed in the field they should be hand threaded (prior to use of power tools) to ensure proper engagement of the thread when re-installing. Failure to pre-start threads may result in cross-threading or stripping of the bolts during reinstallation.</li>
    <li><svg viewBox="0 0 10 10"><rect x="0.7" y="0.7" width="8.6" height="8.6" fill="none" stroke="#1a3d8a" stroke-width="1.2"/><path d="M2.3 5l2 2 4-5" fill="none" stroke="#1a3d8a" stroke-width="1.4"/></svg>The luminaire is designed for outdoor use only</li>
    <li><svg viewBox="0 0 10 10"><rect x="0.7" y="0.7" width="8.6" height="8.6" fill="none" stroke="#1a3d8a" stroke-width="1.2"/><path d="M2.3 5l2 2 4-5" fill="none" stroke="#1a3d8a" stroke-width="1.4"/></svg>The light source contained in this luminaire shall only be replaced by the manufacturer or his service agent or a similarly qualified person.</li>
  </ul>
  <h2 class="abs section-title" style="left:35px;top:286px"><b>IMPORTANT</b> NOTICE</h2>
  <table class="abs spec-table">
    <colgroup><col style="width:93px"><col style="width:57px"><col style="width:56px"><col style="width:56px"><col style="width:55px"><col style="width:56px"><col style="width:52px"></colgroup>
    <thead><tr><th>MODEL</th><th>RATED VOLTAGE, VAC</th><th>FREQUENCY, HZ</th><th>RATED CURRENT, MAX. A</th><th>RATED WATTAGE, W</th><th>UNIT TYPE</th><th>LOCATIONS USE</th></tr></thead>
    <tbody>
      <tr><td class="shade">TLXXX-YY-ZZ-U-V-T</td><td class="shade">120-277</td><td class="shade">50/60</td><td class="shade">0.45</td><td class="shade">30-45</td><td class="merged" rowspan="8">Pole<br>mounted</td><td class="merged" rowspan="8">Wet</td></tr>
      <tr><td class="shade">TLXXX-YY-ZZ-U-V-T</td><td class="shade">120-277</td><td class="shade">50/60</td><td class="shade">0.65</td><td class="shade">45-65</td></tr>
      <tr><td class="shade">TLXXX-YY-ZZ-U-V-T</td><td class="shade">120-277</td><td class="shade">50/60</td><td class="shade">0.85</td><td class="shade">65-85</td></tr>
      <tr><td class="shade">TLXXX-YY-ZZ-U-V-T</td><td class="shade">120-277</td><td class="shade">50/60</td><td class="shade">1.10</td><td class="shade">85-110</td></tr>
      <tr><td class="shade">TLXXX-YY-ZZ-U-V-T</td><td class="shade">120-277</td><td class="shade">50/60</td><td class="shade">1.30</td><td class="shade">100-130</td></tr>
      <tr><td class="shade">TLXXX-YY-ZZ-U-V-T</td><td class="shade">120-277</td><td class="shade">50/60</td><td class="shade">1.60</td><td class="shade">125-165</td></tr>
      <tr><td class="shade">TLXXX-YY-ZZ-U-V-T</td><td class="shade">120-277</td><td class="shade">50/60</td><td class="shade">2.00</td><td class="shade">150-200</td></tr>
      <tr><td class="shade">TLXXX-YY-ZZ-U-V-T</td><td class="shade">120-277</td><td class="shade">50/60</td><td class="shade">2.50</td><td class="shade">200-250</td></tr>
    </tbody>
  </table>
  <div class="abs page-number">2</div>
  <div class="abs page-url">quorivanta.co.nz</div>
</section>

<!-- Nomenclature -->
<section class="page page--nomenclature">
  <h2 class="abs section-title" style="left:33px;top:43px"><b>NOMENCLATURE</b></h2>
  <table class="abs nomen-table">
    <colgroup><col style="width:128px"><col><col><col><col><col><col><col></colgroup>
    <tr><td class="label">EXAMPLE</td><td>TL</td><td>045</td><td>2M</td><td>CW</td><td>U</td><td>P</td><td>G</td></tr>
    <tr><td class="label">GROUP</td><td>TL</td><td>XXX</td><td>YY</td><td>ZZ</td><td>U</td><td>P</td><td>G</td></tr>
  </table>
  <table class="abs group-table">
    <thead><tr><th style="width:77px">GROUP</th><th>DESCRIPTION</th></tr></thead>
    <tbody>
      <tr><td class="code">TL</td><td class="desc">Series name;</td></tr>
      <tr><td class="code">XXX</td><td class="desc">Represent lamp wattage,may be any number, e.g. 045=45W;</td></tr>
      <tr><td class="code">YY</td><td class="desc">Represent the optics model number;</td></tr>
      <tr><td class="code">ZZ</td><td class="desc">Represent color temperature,may be CW - Cool White; NW- Neutral White; WW- Warm White; MW -Mesopic.</td></tr>
      <tr><td class="code">U</td><td class="desc">Represents input voltage is 120-277V;</td></tr>
      <tr><td class="code">V</td><td class="desc">Represents dimming function, may be P -Photocell; D - DALI; Z - 0-10V.</td></tr>
      <tr><td class="code">T</td><td class="desc">Represents lamp color, may beG - Gray; B- Black; W - White.</td></tr>
    </tbody>
  </table>
  <h2 class="abs section-title" style="left:33px;top:417px"><b>LIGHTING</b> DISTRIBUTION TYPES</h2>
  <div class="abs chart-caption" style="left:60px;top:456px">Type II Medium</div>
  <div class="abs chart-caption" style="left:261px;top:456px">Type NEMA 3x3</div>
  <div class="abs chart" style="left:76px;top:475px;width:110px;height:58px" role="img" aria-label="Polar light distribution curve, Type II Medium"></div>
  <div class="abs chart" style="left:276px;top:475px;width:110px;height:58px" role="img" aria-label="Polar light distribution curve, Type NEMA 3x3"></div>
  <div class="abs chart-caption" style="left:60px;top:558px">Type II Medium</div>
  <div class="abs chart-caption" style="left:261px;top:558px">Type III Medium</div>
  <div class="abs chart" style="left:73px;top:578px;width:111px;height:63px" role="img" aria-label="Isolux footprint diagram, Type II Medium"></div>
  <div class="abs chart" style="left:274px;top:578px;width:111px;height:63px" role="img" aria-label="Isolux footprint diagram, Type III Medium"></div>
  <div class="abs page-number" style="left:33px">3</div>
  <div class="abs page-url">quorivanta.co.nz</div>
</section>

<!-- Back cover -->
<section class="page page--back">
  <svg class="page-shapes" viewBox="0 0 424 600" preserveAspectRatio="none" aria-hidden="true">
    <polygon points="257,321 424,400 424,470" fill="#0b3a75"/>
    <polygon points="0,458 257,321 0,600" fill="#0b3a75"/>
    <polygon points="257,321 424,470 424,600 20,600" fill="#ffffff"/>
  </svg>
  <div class="abs back-mark"><span class="wordmark wordmark--light">Quorivanta</span></div>
  <div class="abs contact-row">
    <div class="contact-item"><svg viewBox="0 0 10 10"><path d="M5 0.5a3.3 3.3 0 0 0-3.3 3.3C1.7 6.3 5 9.5 5 9.5s3.3-3.2 3.3-5.7A3.3 3.3 0 0 0 5 .5z" fill="#0b3a75"/><circle cx="5" cy="3.8" r="1.2" fill="#fff"/></svg><span>18 Harrowgate Ln, Kelburn Vale,<br>Wellington 6099, New Zealand</span></div>
    <div class="contact-item"><svg viewBox="0 0 10 10"><path d="M1 3c0-1 1-2 4-2s4 1 4 2v1H7V3H3v1H1z M2 5h6l1 4H1z" fill="#0b3a75"/></svg><span>04 555 0172</span></div>
    <div class="contact-item"><svg viewBox="0 0 10 10"><rect x="0.5" y="2" width="9" height="6" fill="none" stroke="#0b3a75"/><path d="M.5 2l4.5 3.5L9.5 2" fill="none" stroke="#0b3a75"/></svg><span>info@quorivanta.co.nz</span></div>
    <div class="contact-item"><svg viewBox="0 0 10 10"><circle cx="5" cy="5" r="4.3" fill="none" stroke="#0b3a75"/><ellipse cx="5" cy="5" rx="1.8" ry="4.3" fill="none" stroke="#0b3a75"/><path d="M.7 5h8.6" stroke="#0b3a75"/></svg><span>quorivanta.co.nz</span></div>
  </div>
</section>

</body>
</html>
```